Survey App for phone users trying a new phone with Dual connectivity

Survey App Brief<br/>Design For an Android Survey App for users' feedback on Call, SMS, Data and Streaming Experience on their Mobile phones.<br/><br/>Purpose of the App<br/>To ensure that the user's experience is not impacted by the network switching between two network on the special mobile phones they newly started using.<br/><br/>App Requirements:<br/>First screen: The registration screen, where the user needs to enter the following:<br/>Name: text box<br/>Phone Number: text box<br/>Group Number : <br/><br/>An information text:<br/>By Registering I agree to participate in the Survey.<br/><br/>Register: Button<br/><br/>Start Screen - Survey screens (next time user open the App this will be the first screen):<br/>We need feedback for 4 indicators:<br/>Call Experience<br/>SMS Experience<br/>Data Experience<br/>Streaming Experience<br/><br/>Each Experience can be in the form of a questionnaire or Satisfied/ Somewhat Satisfied / Extremely Satisfied form with radio buttons or on a scale of 1 to 5. We need to ensure that the format used is very professional.<br/><br/>An optional text box for the user to enter the comment in a free format.<br/><br/>This can be done in 4 different screens or in one single screen if it does not give a clumsy look.<br/><br/>A Send button at the end to submit the Survey.<br/><br/>We need a burger menu at the top left corner of this screen, which when expanded will provide 5 options:<br/>Edit User Profile<br/>Survey interval Timer<br/>FAQ<br/>Exit<br/>About<br/><br/><br/>Please ensure that the app is simple, friendly, lively and professional at the same time so that it ignites an interest in the user to use the app.<br/>Use Logo as appropriate.
Telecommunications
Colors
Designer to choose colors to be used in the design.

```html
<!DOCTYPE html>
<html lang="en">
<head>
<meta charset="utf-8">
<title>Survey App – Screens</title>
<link href="https://fonts.googleapis.com/css2?family=Poppins:wght@400;500;600;700&display=swap" rel="stylesheet">
<style>
:root{
  --page:#f4f6fb;
  --blob:#e8ecf6;
  --screen:#ffffff;
  --screen-soft:#f3f5fa;
  --field:#f0f3fa;
  --ink:#1d2a4a;
  --muted:#8a93a8;
  --blue:#3aa4e0;
  --blue-deep:#0f6fd3;
  --blue-light:#42c6ea;
  --track:#dfe6f1;
  --highlight:#eaf3fc;
  --shade:rgba(120,130,150,.45);
}
*{box-sizing:border-box;margin:0;padding:0}
html,body{width:1200px;height:2808px;overflow:hidden}
body{background:var(--page);font-family:"Poppins",sans-serif;color:var(--ink);position:relative}
.blob{position:absolute;border-radius:50%;background:var(--blob)}
.blob--one{width:1500px;height:1500px;left:-620px;top:1720px}
.blob--two{width:700px;height:700px;right:-260px;top:1280px;opacity:.6}

.brand{position:absolute;left:408px;top:96px;width:384px;height:160px;background:#fff;display:flex;align-items:center;justify-content:center;gap:18px}
.brand__mark{width:40px;height:40px;background:var(--blue)}
.brand__name{font-weight:600;font-size:30px;color:var(--blue-deep);letter-spacing:1px;line-height:1.1;text-transform:uppercase}

.phone{position:absolute;width:440px;background:var(--screen);border-radius:8px;box-shadow:0 20px 50px rgba(40,60,110,.08);overflow:hidden}
.phone--register{left:104px;top:408px;height:1088px}
.phone--survey{left:648px;top:408px;height:1360px;background:var(--screen-soft)}
.phone--menu{left:104px;top:1536px;height:992px}

.status{position:absolute;left:0;right:0;top:0;height:44px;display:flex;align-items:center;justify-content:space-between;padding:0 22px;font-weight:600;font-size:15px}
.home-bar{position:absolute;bottom:16px;left:50%;width:140px;height:5px;margin-left:-70px;border-radius:3px;background:var(--ink)}

.mini-brand{position:absolute;left:50%;transform:translateX(-50%);display:flex;align-items:center;gap:6px;font-size:11px;font-weight:600;color:var(--blue-deep);text-transform:uppercase;white-space:nowrap}
.mini-brand i{width:14px;height:14px;background:var(--blue);display:block}

.register__title{position:absolute;left:36px;top:150px;font-size:36px;font-weight:700}
.field{position:absolute;left:28px;width:388px;height:60px;border-radius:30px;background:var(--field);display:flex;align-items:center;gap:18px;padding-left:22px;font-size:17px;color:#5a6580}
.field svg{width:22px;height:22px}
.register__note{position:absolute;left:60px;right:60px;top:770px;text-align:center;font-size:14px;color:var(--muted);line-height:1.4}
.btn{position:absolute;border-radius:30px;background:var(--blue);color:#fff;font-weight:600;font-size:15px;display:flex;align-items:center;justify-content:center;letter-spacing:.5px;text-transform:uppercase}
.register__btn{left:28px;width:388px;top:840px;height:58px}

.burger{position:absolute;left:24px;top:66px;width:28px}
.burger span{display:block;height:3px;background:var(--ink);margin-bottom:6px;border-radius:2px}
.survey__lead{position:absolute;left:0;right:0;top:128px;text-align:center;font-size:18px;font-weight:600}
.card{position:absolute;left:18px;width:404px;height:236px;background:#fff;border-radius:14px;box-shadow:0 6px 18px rgba(40,60,110,.06)}
.card__title{position:absolute;left:22px;top:22px;font-size:20px;font-weight:600}
.card__na{position:absolute;right:20px;top:22px;display:flex;align-items:center;gap:8px;font-size:13px;color:var(--muted)}
.radio{width:22px;height:22px;border-radius:50%;border:2px solid #b7c0d2;position:relative}
.radio--on{border-color:var(--blue-deep)}
.radio--on::after{content:"";position:absolute;inset:4px;border-radius:50%;background:var(--blue-deep)}
.track{position:absolute;left:22px;right:22px;top:84px;height:12px;border-radius:6px;background:var(--track)}
.track__fill{position:absolute;left:0;top:0;bottom:0;border-radius:6px;background:linear-gradient(90deg,var(--blue-deep),var(--blue-light))}
.track__thumb{position:absolute;top:-9px;width:30px;height:30px;margin-left:-15px;border-radius:50%;background:var(--blue);box-shadow:0 2px 6px rgba(15,111,211,.35)}
.scale{position:absolute;left:14px;right:14px;top:112px;display:flex;justify-content:space-between;font-size:11px;color:var(--muted)}
.scale .is-active{color:var(--blue-deep);font-weight:600}
.feedback{position:absolute;left:22px;right:22px;top:152px;height:54px;border-radius:27px;background:#e9ecf3;display:flex;align-items:center;padding-left:24px;font-size:14px;color:var(--muted)}
.survey__progress{position:absolute;left:0;right:0;top:1228px;text-align:center;font-size:13px;color:var(--muted)}
.survey__btn{left:18px;width:404px;top:1268px;height:58px;font-size:17px}

.drawer{position:absolute;left:0;top:0;bottom:0;width:368px;background:#fff;z-index:2;box-shadow:6px 0 20px rgba(40,60,110,.08)}
.menu{position:absolute;left:14px;right:14px;top:150px;list-style:none}
.menu li{height:60px;display:flex;align-items:center;gap:22px;padding-left:22px;font-size:16px;font-weight:500;border-radius:30px;margin-bottom:16px}
.menu li svg{width:20px;height:20px}
.menu li.is-active{background:var(--highlight);color:var(--blue-deep)}
.peek{position:absolute;left:368px;top:0;bottom:0;right:0;background:var(--screen-soft)}
.peek__card{position:absolute;left:14px;width:120px;height:236px;background:#fff;border-radius:14px}
.peek__card b{position:absolute;left:18px;top:22px;font-size:20px;font-weight:600}
.peek__card i{position:absolute;left:18px;right:0;top:84px;height:12px;border-radius:6px 0 0 6px;background:linear-gradient(90deg,var(--blue-deep),var(--blue-light))}
.peek__card u{position:absolute;left:18px;top:152px;width:54px;height:54px;border-radius:27px;background:#e9ecf3}
.peek__shade{position:absolute;inset:0;background:var(--shade)}
.peek .burger{left:16px}
</style>
</head>
<body>
<div class="blob blob--one"></div>
<div class="blob blob--two"></div>

<header class="brand">
  <span class="brand__mark"></span>
  <span class="brand__name">Meridian<br>Telecom</span>
</header>

<!-- Registration -->
<section class="phone phone--register">
  <div class="status"><span>9:41</span>
    <svg width="64" height="14" viewBox="0 0 64 14"><rect x="0" y="9" width="3" height="5" fill="#1d2a4a"/><rect x="5" y="6" width="3" height="8" fill="#1d2a4a"/><rect x="10" y="3" width="3" height="11" fill="#1d2a4a"/><rect x="15" y="0" width="3" height="14" fill="#1d2a4a"/><path d="M24 5a10 10 0 0 1 14 0M27 8a6 6 0 0 1 8 0" stroke="#1d2a4a" stroke-width="2" fill="none"/><rect x="42" y="1" width="19" height="11" rx="3" stroke="#1d2a4a" fill="none"/><rect x="44" y="3" width="15" height="7" rx="1" fill="#1d2a4a"/></svg>
  </div>
  <div class="mini-brand" style="top:74px"><i></i>Meridian Telecom</div>
  <h1 class="register__title">Registration.</h1>
  <div class="field" style="top:304px"><svg viewBox="0 0 24 24" fill="none" stroke="#3aa4e0" stroke-width="2"><circle cx="12" cy="8" r="4"/><path d="M4 21c1-5 15-5 16 0"/></svg>Name</div>
  <div class="field" style="top:384px"><svg viewBox="0 0 24 24" fill="none" stroke="#3aa4e0" stroke-width="2"><path d="M5 3h4l2 5-3 2a12 12 0 0 0 6 6l2-3 5 2v4a2 2 0 0 1-2 2A17 17 0 0 1 3 5a2 2 0 0 1 2-2z"/></svg>Phone Number</div>
  <div class="field" style="top:464px"><svg viewBox="0 0 24 24" fill="none" stroke="#3aa4e0" stroke-width="2"><circle cx="9" cy="8" r="3"/><path d="M3 20c0-4 12-4 12 0M16 5a3 3 0 0 1 0 6M18 15c2 1 3 3 3 5"/></svg>Group Number</div>
  <p class="register__note">By Registering I agree to participate in the Survey</p>
  <div class="btn register__btn">Register</div>
  <div class="home-bar"></div>
</section>

<!-- Survey -->
<section class="phone phone--survey">
  <div class="status"><span>9:41</span>
    <svg width="64" height="14" viewBox="0 0 64 14"><rect x="0" y="9" width="3" height="5" fill="#1d2a4a"/><rect x="5" y="6" width="3" height="8" fill="#1d2a4a"/><rect x="10" y="3" width="3" height="11" fill="#1d2a4a"/><rect x="15" y="0" width="3" height="14" fill="#1d2a4a"/><path d="M24 5a10 10 0 0 1 14 0M27 8a6 6 0 0 1 8 0" stroke="#1d2a4a" stroke-width="2" fill="none"/><rect x="42" y="1" width="19" height="11" rx="3" stroke="#1d2a4a" fill="none"/><rect x="44" y="3" width="15" height="7" rx="1" fill="#1d2a4a"/></svg>
  </div>
  <div class="burger"><span></span><span></span><span></span></div>
  <div class="mini-brand" style="top:74px"><i></i>Meridian Telecom</div>
  <p class="survey__lead">We need feedback for survey</p>

  <article class="card" style="top:176px">
    <h2 class="card__title">Call Experience</h2>
    <div class="card__na">NA<span class="radio"></span></div>
    <div class="track"><div class="track__fill" style="width:75%"></div><div class="track__thumb" style="left:75%"></div></div>
    <div class="scale"><span>Poor</span><span>Not Good</span><span>Neutral</span><span class="is-active">Satisfied</span><span>Very Satisfied</span></div>
    <div class="feedback">Write for feedback</div>
  </article>

  <article class="card" style="top:436px">
    <h2 class="card__title">SMS Experience</h2>
    <div class="card__na">NA<span class="radio"></span></div>
    <div class="track"><div class="track__fill" style="width:50%"></div><div class="track__thumb" style="left:50%"></div></div>
    <div class="scale"><span>Poor</span><span>Not Good</span><span class="is-active">Neutral</span><span>Satisfied</span><span>Very Satisfied</span></div>
    <div class="feedback">Write for feedback</div>
  </article>

  <article class="card" style="top:704px">
    <h2 class="card__title">Data Experience</h2>
    <div class="card__na">NA<span class="radio radio--on"></span></div>
    <div class="track"></div>
    <div class="scale"><span>Poor</span><span>Not Good</span><span>Neutral</span><span>Satisfied</span><span>Very Satisfied</span></div>
    <div class="feedback">Write for feedback</div>
  </article>

  <article class="card" style="top:968px">
    <h2 class="card__title">Streaming Experience</h2>
    <div class="card__na">NA<span class="radio"></span></div>
    <div class="track"><div class="track__fill" style="width:100%"></div><div class="track__thumb" style="left:100%"></div></div>
    <div class="scale"><span>Poor</span><span>Not Good</span><span>Neutral</span><span>Satisfied</span><span class="is-active">Very Satisfied</span></div>
    <div class="feedback">Write for feedback</div>
  </article>

  <p class="survey__progress">4 of 5 Survey Answered</p>
  <div class="btn survey__btn">Submit</div>
  <div class="home-bar"></div>
</section>

<!-- Menu -->
<section class="phone phone--menu">
  <div class="peek">
    <div class="burger" style="top:66px"><span></span><span></span><span></span></div>
    <div class="peek__card" style="top:176px"><b>Call</b><i></i><u></u></div>
    <div class="peek__card" style="top:436px"><b>SMS</b><i></i><u></u></div>
    <div class="peek__card" style="top:704px"><b>Data</b><i></i><u></u></div>
    <div class="peek__shade"></div>
  </div>
  <nav class="drawer">
    <div class="status"><span>9:41</span></div>
    <div class="mini-brand" style="top:74px"><i></i>Meridian Telecom</div>
    <ul class="menu">
      <li><svg viewBox="0 0 24 24" fill="none" stroke="#1d2a4a" stroke-width="2"><rect x="3" y="3" width="7" height="7"/><rect x="14" y="3" width="7" height="7"/><rect x="3" y="14" width="7" height="7"/><rect x="14" y="14" width="7" height="7"/></svg>Dashboard</li>
      <li><svg viewBox="0 0 24 24" fill="none" stroke="#1d2a4a" stroke-width="2"><path d="M4 20h4L19 9l-4-4L4 16z"/></svg>Edit Profiles</li>
      <li class="is-active"><svg viewBox="0 0 24 24" fill="none" stroke="#0f6fd3" stroke-width="2"><path d="M4 12l5 5L20 6"/></svg>Survey Interval Timer</li>
      <li><svg viewBox="0 0 24 24" fill="none" stroke="#1d2a4a" stroke-width="2"><circle cx="6" cy="12" r="2.5"/><circle cx="18" cy="5" r="2.5"/><circle cx="18" cy="19" r="2.5"/><path d="M8 11l8-5M8 13l8 5"/></svg>Share this App</li>
      <li><svg viewBox="0 0 24 24" fill="none" stroke="#1d2a4a" stroke-width="2"><rect x="3" y="5" width="18" height="14" rx="2"/><path d="M3 7l9 6 9-6"/></svg>Contact Us</li>
      <li><svg viewBox="0 0 24 24" fill="none" stroke="#1d2a4a" stroke-width="2"><circle cx="12" cy="12" r="9"/><path d="M3 12h18M12 3c3 3 3 15 0 18M12 3c-3 3-3 15 0 18"/></svg>Help</li>
      <li><svg viewBox="0 0 24 24" fill="none" stroke="#1d2a4a" stroke-width="2"><circle cx="12" cy="12" r="3"/><path d="M12 2v3M12 19v3M2 12h3M19 12h3M5 5l2 2M17 17l2 2M5 19l2-2M17 7l2-2"/></svg>Exit</li>
    </ul>
  </nav>
  <div class="home-bar" style="z-index:3"></div>
</section>
</body>
</html>
```